Bryncarn foot health or foot health bryncarn

Treatments in comfort of your own home
Delia Marsh cert KTLFr Pod, BGNVect
Treatments will be listed on the leaflet I will attach
I am a Foot Health practitioner,
I want to mention I do home visits throughout Pembrokeshire & Ceredigion.
Tel. 07730915264
I have 2 logs to forward to you they are the associations I belong to .
One of which is also a certification mark. It is important that the same colour is used for this mark. They are not the main focus, they are just recognised mark. To be at the top or bottom of the page.
There is a local business called Glenmorrow foot clinic, so my business has to be bryncarn foot health, or foot health bryncarn
soon I will also need a web page and cards designed, so please keep this in mind when designing the Artwork. I will also need an email on the leaflet but I will wait and see what the design is first before I confirm it as I have several.
I hope this is enough info for you.
Many thanks,
Delia Marsh

Target Market(s)

Mostly the elderly, some middle age women, but it is a service for all ages. The elderly are my main clients.

Industry/Entity Type

Health

Font styles to use
Serif
Sans Serif

Colors

Designer to choose colors to be used in the design.

Requirements
Must have
• Covering Pembrokeshire & Ceredigion.
Treatments include:- as listed on example leaflet I sent
Phone number a size that's easily readable.
I am open to colours. I love bright colours, but also like the more conservative colours as long as it looks professional. I'm wanting it to look more up market.
Nice to have
• Logo for Covenant and KTS logo obviously smaller, but also recognisable and either at the top of page or bottom. These are not to be main focal point.

```html
<!DOCTYPE html>
<html lang="en">
<head>
<meta charset="utf-8">
<title>Bryncarn Foothealth</title>
<link rel="stylesheet" href="https://fonts.googleapis.com/css2?family=Lobster&family=Noto+Serif:ital,wght@0,400;1,400;1,700&display=swap">
<style>
:root{
  --paper-light:#fdeedb;
  --paper-edge:#f9b06a;
  --brown:#6a1f0e;
  --brown-deep:#5a2414;
  --gold:#c48a1a;
  --gold-dark:#9a6a1c;
  --tan:#8a6a34;
  --ornament:#e8b868;
  --swirl:rgba(255,245,230,.55);
  --member-green:#2f7a3a;
  --cert-purple:#4b2a9a;
  --white:#ffffff;
}
*{margin:0;padding:0;box-sizing:border-box}
html,body{width:846px;height:1200px;overflow:hidden}
body{background:var(--paper-light)}
.leaflet{
  position:relative;width:846px;height:1200px;overflow:hidden;
  background:radial-gradient(ellipse 70% 60% at 50% 50%,var(--paper-light) 45%,#fcd3a3 80%,var(--paper-edge) 100%);
  font-family:"Noto Serif",Georgia,serif;
}
.swirl-band{position:absolute;left:0;top:300px;width:846px;height:520px}
.ornament{position:absolute;background:linear-gradient(135deg,var(--ornament),#f3cf8c);opacity:.5;border-radius:40px}
.ornament--tl{left:18px;top:18px;width:150px;height:240px;border-radius:8px 60px 60px 60px}
.ornament--r{right:0;top:292px;width:150px;height:175px}
.ornament--l{left:0;top:750px;width:225px;height:210px}
.ornament--br{right:16px;bottom:14px;width:220px;height:250px;border-radius:60px 60px 8px 60px}
.brand{position:absolute;left:0;width:846px;text-align:center;font-family:"Lobster",cursive}
.brand__name{top:96px;font-size:68px;color:var(--brown);text-shadow:0 2px 2px rgba(90,30,10,.25)}
.brand__sub{top:170px;font-size:72px;color:var(--gold);text-shadow:0 2px 2px rgba(120,70,10,.3)}
.rule{position:absolute;left:162px;top:265px;width:520px;height:1px;background:#d7b07a}
.tagline{position:absolute;left:0;top:282px;width:846px;text-align:center;font-style:italic;font-size:23px;color:var(--tan)}
.treatments__title{position:absolute;left:190px;top:386px;font-family:"Lobster",cursive;font-size:52px;color:var(--brown);text-shadow:0 2px 2px rgba(90,30,10,.25)}
.treatments__list{position:absolute;left:198px;top:462px;list-style:none}
.treatments__item{display:flex;align-items:center;height:48.3px;font-size:32px;color:var(--brown-deep)}
.treatments__item svg{width:16px;height:16px;margin-right:14px}
.coverage{position:absolute;left:497px;top:725px;width:186px;height:172px}
.coverage__text{position:absolute;left:497px;top:781px;width:186px;text-align:center;color:var(--white);font-style:italic;font-weight:700;line-height:1.2}
.coverage__lead{font-size:18px}
.coverage__area{font-size:13px;margin-top:4px}
.contact{position:absolute;right:143px;text-align:right}
.contact__name{top:926px;font-family:"Lobster",cursive;font-size:46px;color:var(--brown)}
.contact__cert{top:981px;font-style:italic;font-weight:700;font-size:24px;color:var(--gold)}
.contact__role{top:1011px;font-style:italic;font-size:25px;color:var(--gold-dark)}
.contact__phone{top:1043px;font-family:"Lobster",cursive;font-size:47px;color:var(--gold-dark);letter-spacing:1px}
.contact__note{top:1096px;font-style:italic;font-size:22px;color:var(--brown-deep)}
.membership{position:absolute;left:70px;top:1005px;width:116px;height:116px}
.membership__url{position:absolute;left:58px;top:1125px;width:140px;text-align:center;font-size:9px;color:#333}
.certification{position:absolute;left:226px;top:1064px;width:46px;height:46px}
</style>
</head>
<body>
<main class="leaflet">
  <svg class="swirl-band" viewBox="0 0 846 520" aria-hidden="true">
    <path d="M0 230 C200 80 420 40 620 80 C760 110 846 60 846 20 L846 130 C760 180 620 150 470 160 C300 170 140 260 0 330 Z" fill="var(--swirl)"/>
    <path d="M0 420 C180 330 360 320 560 360 C700 390 800 380 846 350 L846 400 C760 440 620 430 480 420 C300 410 150 460 0 500 Z" fill="var(--swirl)"/>
  </svg>
  <div class="ornament ornament--tl" role="img" aria-label="Gold grapevine corner ornament"></div>
  <div class="ornament ornament--r" role="img" aria-label="Gold scroll ornament"></div>
  <div class="ornament ornament--l" role="img" aria-label="Gold scroll ornament"></div>
  <div class="ornament ornament--br" role="img" aria-label="Gold grapevine corner ornament"></div>

  <h1 class="brand brand__name">Bryncarn</h1>
  <p class="brand brand__sub">Foothealth</p>
  <div class="rule"></div>
  <p class="tagline">Treatments in comfort of your own home</p>

  <h2 class="treatments__title">Treatments Include:</h2>
  <ul class="treatments__list">
    <li class="treatments__item"><svg viewBox="0 0 16 16"><path d="M2 8 L6 12 L14 4" fill="none" stroke="var(--brown)" stroke-width="2.5"/></svg>Diabetic Footcare</li>
    <li class="treatments__item"><svg viewBox="0 0 16 16"><path d="M2 8 L6 12 L14 4" fill="none" stroke="var(--brown)" stroke-width="2.5"/></svg>Ingrowing Toenails</li>
    <li class="treatments__item"><svg viewBox="0 0 16 16"><path d="M2 8 L6 12 L14 4" fill="none" stroke="var(--brown)" stroke-width="2.5"/></svg>Corn &amp; Callous Treatment</li>
    <li class="treatments__item"><svg viewBox="0 0 16 16"><path d="M2 8 L6 12 L14 4" fill="none" stroke="var(--brown)" stroke-width="2.5"/></svg>Toenail Clipping</li>
    <li class="treatments__item"><svg viewBox="0 0 16 16"><path d="M2 8 L6 12 L14 4" fill="none" stroke="var(--brown)" stroke-width="2.5"/></svg>Fungal Infections Treated</li>
    <li class="treatments__item"><svg viewBox="0 0 16 16"><path d="M2 8 L6 12 L14 4" fill="none" stroke="var(--brown)" stroke-width="2.5"/></svg>Cracked Heels</li>
  </ul>

  <svg class="coverage" viewBox="0 0 186 172" aria-hidden="true">
    <g fill="var(--brown-deep)">
      <ellipse cx="93" cy="86" rx="80" ry="72"/>
      <circle cx="93" cy="16" r="16"/><circle cx="93" cy="156" r="16"/>
      <circle cx="16" cy="86" r="16"/><circle cx="170" cy="86" r="16"/>
      <circle cx="38" cy="36" r="16"/><circle cx="148" cy="36" r="16"/>
      <circle cx="38" cy="136" r="16"/><circle cx="148" cy="136" r="16"/>
    </g>
    <ellipse cx="93" cy="86" rx="72" ry="65" fill="none" stroke="var(--white)" stroke-width="1.5"/>
  </svg>
  <div class="coverage__text">
    <p class="coverage__lead">Home visits<br>Troughout</p>
    <p class="coverage__area">Pembrokeshire &amp;<br>Ceredigion.</p>
  </div>

  <p class="contact contact__name">Delia Marsh</p>
  <p class="contact contact__cert">cert .KTLFr Pod, BGNVect</p>
  <p class="contact contact__role">Foot Health practitioner</p>
  <p class="contact contact__phone">077 3091 5264</p>
  <p class="contact contact__note">Home visit by Arragement</p>

  <svg class="membership" viewBox="0 0 116 116" aria-hidden="true">
    <circle cx="58" cy="58" r="56" fill="var(--member-green)"/>
  </svg>
  <p class="membership__url">www.thecovenantpsp.com</p>
  <svg class="certification" viewBox="0 0 46 46" aria-hidden="true">
    <circle cx="23" cy="23" r="22" fill="var(--cert-purple)"/>
  </svg>
</main>
</body>
</html>
```